Website development

Looking for a simple website, containing circa 10-15 pages of brochure-ware content for our new Cafe and Farm Shop venture.

We have a logo, designed through this site, which we think is really strong.

The Cafe and Farm Shop are all about locally sourced, high quality food served in a stunning rural location by happy, friendly staff. Great quality food and drink at sensible prices.

Initially the website needs to contain 10 or so pages of content, which ideally we would like to manage on-going (perhaps not every page, but as many pages as the budget will allow). We want to make sure that the website stays fresh and current and so we want a basic CMS to keep the text areas updated.

We would also like a simple data capture page, so that we can start to generate a database of email addresses for our on-going marketing efforts. Any thoughts around a basic CRM tool gratefully received.

The creative brief can take some inspiration from the logo, but should be bright, clean, welcoming and engaging. Not too over-bearing with colours or content. Fun, easy and interesting to use with all the text and image information clearly displayed.

We don't currently have any imagery beyond the logo, and would like to use as much free stock photography and imagery as possible. If needs be we can take some good quality pictures and provide them.

We're in the process of purchasing the URL(s) at present and will supply them in due course, but they will be based around the trading name.

If you have any more questions please do not hesitate to contact me.

Many thanks
Owen

Industry/Entity Type

Cafe

```html
<!DOCTYPE html>
<html lang="en">
<head>
<meta charset="utf-8">
<title>The Willow Barn – Cafe and Farm Shop</title>
<link href="https://fonts.googleapis.com/css2?family=Arimo:wght@400;700&display=swap" rel="stylesheet">
<style>
  :root {
    --cyan: #12cadf;
    --green: #1b7a2c;
    --deep-green: #0d5a1c;
    --tweet-green: #4e8a3a;
    --tweet-text: #c9f59a;
    --grey: #8a8a8a;
    --light-grey: #b5b5b5;
    --rule: #ececec;
    --white: #ffffff;
  }
  html, body { margin: 0; padding: 0; overflow: hidden; background: var(--white); }
  .canvas {
    position: relative; width: 1200px; height: 1000px; overflow: hidden;
    font-family: "Arimo", Arial, sans-serif; background: var(--white);
  }
  .abs { position: absolute; }

  /* Header */
  .brand { left: 283px; top: 58px; display: flex; align-items: center; gap: 8px; }
  .brand-mark { width: 14px; height: 14px; background: var(--green); }
  .brand-name { font-size: 26px; color: var(--green); font-weight: 400; letter-spacing: .2px; }
  .social { top: 17px; left: 926px; display: flex; gap: 4px; }
  .social span { width: 14px; height: 14px; border-radius: 50%; background: var(--cyan); display: block; }
  .contact { right: 243px; top: 38px; text-align: right; font-size: 8px; line-height: 14px; color: var(--light-grey); }
  .main-nav { top: 96px; left: 578px; display: flex; font-size: 13px; }
  .main-nav a { text-decoration: none; color: var(--green); }
  .main-nav a.is-current { color: var(--cyan); }

  /* Category band */
  .category-band { left: 189px; top: 122px; width: 853px; height: 44px; background: var(--cyan); }
  .nav-tab { left: 560px; top: 112px; }
  .category-nav { left: 283px; top: 138px; display: flex; font-size: 13px; color: var(--white); }
  .category-nav .is-current { color: var(--green); }
  .category-nav .sep { margin: 0 28px; }

  /* Hero */
  .hero {
    left: 189px; top: 166px; width: 853px; height: 279px;
    background: radial-gradient(circle at 85% 40%, #f4f8dc 0%, #dfebc4 35%, #c8dca8 100%);
  }
  .hero-image {
    left: 348px; top: 205px; width: 180px; height: 222px; border-radius: 46% 46% 40% 40%;
    background: linear-gradient(180deg, #c7dc6a 0%, #f6c332 30%, #f08a1e 50%, #b8282a 68%, #b9d35a 90%);
  }
  .tweet-bar {
    left: 283px; top: 166px; width: 674px; height: 30px; background: var(--tweet-green);
    border-radius: 0 0 3px 3px; display: flex; align-items: center; font-size: 10px; color: var(--tweet-text);
  }
  .tweet-icon { width: 18px; height: 18px; border-radius: 50%; background: var(--white); margin: 0 20px 0 9px; }
  .tweet-bar strong { color: var(--white); font-weight: 400; }
  .hero-kicker { left: 565px; top: 276px; font-size: 17px; line-height: 21px; color: var(--green); }
  .hero-title { left: 564px; top: 342px; font-size: 36px; color: var(--deep-green); margin: 0; font-weight: 400; }
  .hero-arrow { top: 298px; }
  .hero-dots { left: 881px; top: 420px; display: flex; gap: 2px; }
  .hero-dots span { width: 8px; height: 8px; border-radius: 50%; background: #7ccb84; border: 1px solid var(--green); }
  .hero-dots span.is-active { background: var(--green); }

  /* Intro panel */
  .intro { left: 283px; top: 454px; width: 674px; height: 178px; background: var(--cyan); border-radius: 6px; }
  .intro-image {
    left: 296px; top: 490px; width: 172px; height: 108px; border-radius: 40% 40% 50% 50%;
    background: radial-gradient(ellipse at 50% 35%, #5a2a12 0%, #3b1a0a 40%, #d7e6ea 70%, #a9c4cc 100%);
  }
  .intro-heading { left: 477px; top: 495px; margin: 0; font-size: 17px; font-weight: 400; color: var(--white); }
  .intro-copy { left: 478px; top: 535px; width: 464px; margin: 0; font-size: 9.6px; line-height: 11.6px; color: var(--white); }

  /* Feature columns */
  .feature { top: 664px; width: 160px; text-align: center; }
  .feature h3 { margin: 0; font-size: 13px; font-weight: 700; color: var(--green); }
  .feature-image { width: 72px; height: 68px; margin: 9px auto 10px; border-radius: 12px; }
  .feature p { margin: 0; font-size: 8.5px; line-height: 15px; color: var(--grey); }
  .col-rule { top: 672px; width: 1px; height: 124px; background: var(--rule); }
  .footer-rule { left: 283px; top: 813px; width: 674px; height: 1px; background: var(--rule); }

  /* Footer */
  .footer-col { top: 848px; }
  .footer-col h4 { margin: 0 0 10px; font-size: 12.5px; font-weight: 400; color: var(--grey); }
  .footer-col ul { list-style: none; margin: 0; padding: 0; font-size: 8.5px; line-height: 10.3px; color: var(--grey); }
  .copyright-bar {
    left: 283px; top: 960px; width: 674px; height: 40px; background: var(--cyan);
    border-radius: 6px 6px 0 0; font-size: 8px; color: #e6fbfd; text-align: center; line-height: 30px;
  }
</style>
</head>
<body>
<div class="canvas">

  <header>
    <div class="abs brand"><span class="brand-mark"></span><span class="brand-name">The Willow Barn</span></div>
    <div class="abs social" aria-label="Social links"><span></span><span></span></div>
    <div class="abs contact">Call 020 7946 0321<br>Email: hello@willowbarn.example</div>
    <nav class="abs main-nav">
      <a class="is-current" href="#" style="margin-right:24px">Home</a>
      <a href="#" style="margin-right:11px">About us</a>
      <a href="#" style="margin-right:15px">Services</a>
      <a href="#" style="margin-right:27px">Portfolio</a>
      <a href="#" style="margin-right:14px">News</a>
      <a href="#">Contact Us</a>
    </nav>
  </header>

  <div class="abs category-band"></div>
  <svg class="abs nav-tab" width="70" height="12" viewBox="0 0 70 12" aria-hidden="true">
    <polygon points="10,2 62,10 62,12 10,12" fill="var(--cyan)"/>
  </svg>
  <nav class="abs category-nav">
    <span class="is-current">CORPORATE</span><span class="sep">|</span>
    <span>ECOMMERCE</span><span class="sep">|</span>
    <span>CREATIVE</span><span class="sep">|</span>
    <span>BROUCHURE WEBSITE</span>
  </nav>

  <section>
    <div class="abs hero" role="img" aria-label="Soft green bokeh background"></div>
    <div class="abs hero-image" role="img" aria-label="Stacked slices of apple, orange and lemon"></div>
    <div class="abs tweet-bar">
      <span class="tweet-icon"></span>
      <span>@Tweet: Looking for a @simple website, <strong>&nbsp;containing circa 10-15 pages of&nbsp;</strong> brochure-ware content for our new Cafe and Farm Shop venture.</span>
    </div>
    <div class="abs hero-kicker">The<br>Willow Barn<br>Cafe And Farm Shop</div>
    <h1 class="abs hero-title">Real Taste of Coffee!</h1>
    <svg class="abs hero-arrow" style="left:285px" width="36" height="64" viewBox="0 0 36 64" aria-label="Previous slide">
      <polygon points="22,0 36,0 14,32 36,64 22,64 0,32" fill="#ffffff"/>
    </svg>
    <svg class="abs hero-arrow" style="left:918px" width="36" height="64" viewBox="0 0 36 64" aria-label="Next slide">
      <polygon points="0,0 14,0 36,32 14,64 0,64 22,32" fill="#ffffff"/>
    </svg>
    <div class="abs hero-dots"><span class="is-active"></span><span></span><span></span><span></span></div>
  </section>

  <section>
    <div class="abs intro"></div>
    <div class="abs intro-image" role="img" aria-label="Glass cup of tea on a saucer"></div>
    <h2 class="abs intro-heading">Sub Heading</h2>
    <p class="abs intro-copy">The Cafe and Farm Shop are all about locally sourced, high quality food served in a stunning rural location by happy, friendly staff. Great quality food and drink at sensible prices.&nbsp; The Cafe and Farm Shop are all about locally sourced, high quality food served in a stunning rural location by happy, friendly staff. Great quality food and drink at sensible prices.</p>
  </section>

  <section>
    <div class="abs feature" style="left:289px"><h3>Some Text</h3><div class="feature-image" role="img" aria-label="Burger" style="background:linear-gradient(180deg,#e9a640,#6aa83a 50%,#a2461e)"></div><p>Great quality food and drink at<br>sensible prices.</p></div>
    <div class="abs col-rule" style="left:459px"></div>
    <div class="abs feature" style="left:450px"><h3>Some Text</h3><div class="feature-image" role="img" aria-label="Milk carton and glass of milk" style="background:linear-gradient(90deg,#2b5fb0,#e8eef4 60%,#ffffff)"></div><p>Great quality food and drink at<br>sensible prices.</p></div>
    <div class="abs col-rule" style="left:612px"></div>
    <div class="abs feature" style="left:610px"><h3>Some Text</h3><div class="feature-image" role="img" aria-label="Bowl of noodles with chopsticks" style="background:linear-gradient(180deg,#f2b33a,#e9e3d2 50%,#2b4ea0)"></div><p>Great quality food and drink at<br>sensible prices.</p></div>
    <div class="abs col-rule" style="left:764px"></div>
    <div class="abs feature" style="left:771px"><h3>Some Text</h3><div class="feature-image" role="img" aria-label="Bamboo steamer with buns" style="background:linear-gradient(180deg,#f5eee0,#d59a4a 55%,#a8682a)"></div><p>Great quality food and drink at<br>sensible prices.</p></div>
    <div class="abs footer-rule"></div>
  </section>

  <footer>
    <div class="abs footer-col" style="left:283px"><h4>Corporate</h4><ul><li>About Us</li><li>Career</li><li>Privacy Policy</li><li>News Archiev</li></ul></div>
    <div class="abs footer-col" style="left:427px;top:850px"><h4>Services</h4><ul><li>About Us</li><li>Career</li><li>Privacy Policy</li><li>News Archiev</li><li>More Links</li></ul></div>
    <div class="abs footer-col" style="left:559px;top:850px"><h4>Customer Service</h4><ul><li>About Us</li><li>Career</li><li>Privacy Policy</li><li>News Archiev</li></ul></div>
    <div class="abs footer-col" style="left:719px"><h4>Buying Online</h4><ul><li>About Us</li><li>Career</li><li>Privacy Policy</li><li>News Archiev</li><li>More Links</li></ul></div>
    <div class="abs footer-col" style="left:858px"><h4>Company Profile</h4><ul><li>About Us</li><li>Career</li><li>Privacy Policy</li><li>News Archiev</li></ul></div>
    <div class="abs copyright-bar">Copyright All Right Reserved 2013-14</div>
  </footer>

</div>
</body>
</html>
```